Redesign a TV Station website

Hello,
it looks like my explaination was not clear enough so i would like to clarify.
We are no longer designing a news website but rather a website for our TV station.
Please take a look at the current website we have .
http://www.vko.ci
We want a website similar to these two websites as example.

Please use the following websites as example
https://www.lumatel.com/
https://www.drw.com/

Here are my main menu on the horizontal bar
Accueil | Films | Series | Enfants | TV en Direct
P/S: You should disregard previous designs for the news website. We are designing purely a website for the TV stations. Please take a look at current site we have and design it similar to these two examples i mentioned
https://www.lumatel.com/
https://www.drw.com/
Updates

I needed more info for the project update.

Hello, We have updated design requirement for our project and hope it is much easier for you. You need to design the page based on the content on the link below: http://587opratv.com/template_obs.pdf You should use the same design as this to design the page http://587opratv.com/marc.jpeg The page will have same header style, color and design as the last link. However the content and layout of the page is the same as the first link. Please disregard the section that says "PAGE TYPE POUR MOBILE VERSION" Also disregard the title "MINI SITE LES ARPENTEURS "

Target Market(s)

TV Station

Number of Pages Required

1 page

Font styles to use
Sans Serif

Colors

Designer to choose colors to be used in the design.

Requirements
Must have
• N/A
Nice to have
• N/A
Should not have
• N/A

```html
<!DOCTYPE html>
<html lang="fr">
<head>
<meta charset="utf-8">
<title>Kora Télé — Télévision</title>
<link href="https://fonts.googleapis.com/css2?family=Roboto:wght@400;500;700;900&family=Roboto+Condensed:wght@700&display=swap" rel="stylesheet">
<style>
:root{
  --blue:#0b3a8c;
  --navy:#0a2a6b;
  --orange:#ef6a1f;
  --green:#6cae2f;
  --grey-band:#ececec;
  --text:#222;
  --muted:#777;
  --white:#fff;
  --line:#ddd;
}
*{box-sizing:border-box;margin:0;padding:0}
html,body{width:1200px;height:2992px;overflow:hidden}
body{font-family:"Roboto",sans-serif;color:var(--text);background:var(--white);position:relative}
.wrap{width:1040px;margin:0 auto;position:relative}

/* header */
.topbar{height:132px;display:flex;align-items:center;justify-content:space-between}
.brand{font-weight:700;font-size:30px;color:var(--blue);white-space:nowrap}
.ads{display:flex;gap:20px}
.ad{width:240px;height:64px}
.ad-a{background:linear-gradient(90deg,#1a1a1a,#ef6a1f)}
.ad-b{background:linear-gradient(90deg,#c8102e,#7a0b1c)}
.social{display:flex;gap:8px}
.social span{width:32px;height:32px;border-radius:50%;background:var(--blue);display:block}
.social span:nth-child(2){background:#2aa9e0}
.social span:nth-child(3){background:#d0312d}
.social span:nth-child(4){background:#1f66b1}

.mainnav{height:60px;background:var(--blue);display:flex;align-items:center;padding:0 22px;color:var(--white)}
.mainnav ul{list-style:none;display:flex;gap:48px;margin-left:44px;flex:1}
.mainnav li{font-size:17px;font-weight:500;letter-spacing:.5px}

/* hero */
.hero{height:520px;position:relative;background:linear-gradient(160deg,#8fa3b3 0%,#4d5c6b 45%,#2b2f3a 100%)}
.hero h1{position:absolute;left:90px;bottom:74px;width:620px;font-family:"Roboto Condensed",sans-serif;font-size:42px;line-height:1.1;color:var(--white);text-transform:uppercase}

/* section labels */
.label{display:flex;align-items:center;margin:32px 0 24px}
.label span{color:var(--white);font-weight:700;font-size:17px;padding:14px 22px;text-transform:uppercase}
.label i{flex:1;height:2px}
.label.orange span{background:var(--orange)} .label.orange i{background:var(--orange)}
.label.blue span{background:var(--blue)} .label.blue i{background:var(--blue)}
.label.green span{background:var(--green)} .label.green i{background:var(--green)}

/* news cards */
.news-grid{display:grid;grid-template-columns:repeat(4,1fr);gap:16px}
.news-card{border:1px solid var(--line);height:308px}
.news-card .pic{height:160px;position:relative}
.news-card .tag{position:absolute;left:10px;bottom:-10px;background:var(--orange);color:var(--white);font-size:11px;font-weight:700;padding:4px 10px}
.news-card h3{font-size:15px;line-height:1.3;margin:22px 12px 8px}
.news-card p{font-size:11px;color:var(--muted);line-height:1.45;margin:0 12px 10px}
.date{font-size:10px;color:var(--muted);display:flex;align-items:center;gap:6px}
.date::before{content:"";width:8px;height:8px;background:var(--blue);display:block}
.news-card .date{margin:0 12px}

/* team */
.team{background:var(--grey-band);margin-top:92px;padding:4px 0 60px}
.team-grid{display:grid;grid-template-columns:repeat(4,1fr);gap:16px}
.team-card{background:var(--white);height:240px}
.team-card .pic{height:148px}
.team-card h4{font-size:14px;font-weight:500;margin:16px 12px 10px}
.team-card .date{margin:0 12px}

/* most read */
.top-grid{display:grid;grid-template-columns:repeat(3,1fr);gap:20px}
.top-card .pic{height:232px}
.top-card .row{display:flex;gap:12px;margin-top:16px}
.top-card b{font-size:40px;color:var(--orange);font-weight:700;line-height:1}
.top-card p{font-size:14px;line-height:1.45}

/* links band */
.band{margin-top:110px;height:52px;background:var(--orange);display:flex;justify-content:center;align-items:center;gap:18px;color:var(--white);font-size:15px;font-weight:700;letter-spacing:.6px}

/* partners */
.partners h2{text-align:center;color:var(--blue);font-size:22px;font-weight:900;margin-top:64px;letter-spacing:1px}
.partners ul{list-style:none;display:flex;justify-content:space-between;align-items:center;margin-top:34px;height:90px}
.partners li{display:flex;align-items:center;gap:10px;font-size:22px;font-weight:700;color:var(--navy)}
.partners li .sq{width:34px;height:34px;background:var(--blue)}
.partners li .sq.green{background:var(--green)}
.partners li .ci{width:34px;height:34px;border-radius:50%;background:var(--orange)}

/* footer */
.site-footer{position:absolute;left:0;top:2480px;width:1200px;height:512px;background:var(--navy);color:var(--white)}
.fcols{display:flex;padding-top:68px}
.fcol{width:220px}
.fcol h5{font-size:15px;font-weight:700;margin-bottom:14px;letter-spacing:.5px}
.fcol ul{list-style:none;margin-bottom:38px}
.fcol li{font-size:12px;line-height:1.85;color:#c8d3ea}
.store{width:110px;height:34px;border-radius:6px;background:#000;border:1px solid #888;margin-bottom:12px}
.copy{position:absolute;left:0;right:0;bottom:0;height:66px;border-top:1px solid #2f4b86;text-align:center;font-size:12px;color:#c8d3ea;line-height:66px}
</style>
</head>
<body>
<header class="wrap">
  <div class="topbar">
    <div class="brand">Kora Télé</div>
    <div class="ads">
      <div class="ad ad-a" role="img" aria-label="Bannière publicitaire"></div>
      <div class="ad ad-b" role="img" aria-label="Bannière publicitaire"></div>
    </div>
    <div class="social"><span></span><span></span><span></span><span></span></div>
  </div>
  <nav class="mainnav">
    <svg width="22" height="18" viewBox="0 0 22 18"><rect width="22" height="3" fill="#fff"/><rect y="7.5" width="22" height="3" fill="#fff"/><rect y="15" width="22" height="3" fill="#fff"/></svg>
    <ul><li>ACCUEIL</li><li>FILMS</li><li>SERIES</li><li>ENFANTS</li><li>TV EN DIRECT</li></ul>
    <svg width="20" height="20" viewBox="0 0 20 20"><circle cx="8" cy="8" r="6" fill="none" stroke="#fff" stroke-width="2.5"/><line x1="12.5" y1="12.5" x2="18" y2="18" stroke="#fff" stroke-width="2.5"/></svg>
  </nav>
  <section class="hero" role="img" aria-label="Plateau de télévision avec deux présentateurs et une caméra">
    <h1>Rome: un escalier mécanique s'écroule, une vingtaine de blessés</h1>
  </section>

  <div class="label orange"><span>Les autres titres</span><i></i></div>
  <div class="news-grid">
    <article class="news-card"><div class="pic" style="background:linear-gradient(135deg,#3b4a66,#1d2333)" role="img" aria-label="Photo d'un intervenant en costume"><span class="tag">POLITIQUE</span></div><h3>Corruption et causalité: peut-on décrocher un prix</h3><p>Un débat animé sur la transparence publique et les récentes décisions prises par les institutions du pays.</p><div class="date">Publié le 18 juin 2018</div></article>
    <article class="news-card"><div class="pic" style="background:linear-gradient(135deg,#8a6f9e,#3d3350)" role="img" aria-label="Photo d'une réunion sur scène"><span class="tag">POLITIQUE</span></div><h3>Pourquoi certaines loutres sont-elles homophobes malgré</h3><p>Des chercheurs présentent leurs travaux lors d'une conférence et répondent aux questions du public présent.</p><div class="date">Publié le 18 juin 2018</div></article>
    <article class="news-card"><div class="pic" style="background:linear-gradient(135deg,#5d6f8c,#27324a)" role="img" aria-label="Photo de deux hommes à une tribune"><span class="tag">POLITIQUE</span></div><h3>Corruption et causalité: peut-on décrocher un prix</h3><p>Un débat animé sur la transparence publique et les récentes décisions prises par les institutions du pays.</p><div class="date">Publié le 18 juin 2018</div></article>
    <article class="news-card"><div class="pic" style="background:linear-gradient(135deg,#2a6fb5,#0f2f66)" role="img" aria-label="Photo d'une présentatrice en plateau"><span class="tag">POLITIQUE</span></div><h3>Pourquoi certaines loutres sont-elles homophobes malgré</h3><p>Des chercheurs présentent leurs travaux lors d'une conférence et répondent aux questions du public présent.</p><div class="date">Publié le 18 juin 2018</div></article>
  </div>
</header>

<section class="team">
  <div class="wrap">
    <div class="label blue"><span>L'équipe</span><i></i></div>
    <div class="team-grid">
      <div class="team-card"><div class="pic" style="background:linear-gradient(135deg,#6b5a4a,#2c2520)" role="img" aria-label="Photo de l'équipe des sports"></div><h4>JO3 Le Journal Des sports</h4><div class="date">Publié le 18 juin 2018</div></div>
      <div class="team-card"><div class="pic" style="background:linear-gradient(135deg,#7d8aa0,#333a48)" role="img" aria-label="Photo d'une journaliste en reportage"></div><h4>JO3 Le Journal Des sports</h4><div class="date">Publié le 18 juin 2018</div></div>
      <div class="team-card"><div class="pic" style="background:linear-gradient(135deg,#5a4f6e,#231f2e)" role="img" aria-label="Photo d'un journaliste devant un écran"></div><h4>JO3 Le Journal Des sports</h4><div class="date">Publié le 18 juin 2018</div></div>
      <div class="team-card"><div class="pic" style="background:linear-gradient(135deg,#3a5f9a,#1a2a4a)" role="img" aria-label="Photo de présentateurs en plateau"></div><h4>JO3 Le Journal Des sports</h4><div class="date">Publié le 18 juin 2018</div></div>
    </div>
  </div>
</section>

<section class="wrap">
  <div class="label green"><span>Les plus lus</span><i></i></div>
  <div class="top-grid">
    <div class="top-card"><div class="pic" style="background:linear-gradient(135deg,#8a6a4a,#2a2018)" role="img" aria-label="Photo d'un cameraman filmant"></div><div class="row"><b>1</b><p>Coupe du monde de basket 2019 : les équipes nationales dévoilent leurs listes finales</p></div></div>
    <div class="top-card"><div class="pic" style="background:linear-gradient(135deg,#7a3f8f,#1e1030)" role="img" aria-label="Photo d'une présentatrice sur un plateau éclairé"></div><div class="row"><b>2</b><p>Fraude fiscale : le gouvernement annonce des mesures et un contrôle renforcé</p></div></div>
    <div class="top-card"><div class="pic" style="background:linear-gradient(135deg,#4a4f5c,#0c0d12)" role="img" aria-label="Photo d'un studio de tournage sombre"></div><div class="row"><b>3</b><p>Pesticides : un rapport inquiétant publié sur les cultures et la santé publique</p></div></div>
  </div>
</section>

<div class="band"><span>LES ARPENTEURS</span>|<span>LA COMMUNAUTÉ</span>|<span>NOUS JOINDRE</span>|<span>LA CHARTE</span></div>

<section class="wrap partners">
  <h2>PARTENAIRES</h2>
  <ul>
    <li><span class="ci"></span>Veritas Watch</li>
    <li><span class="sq"></span>Agence Nord</li>
    <li><span class="sq"></span>Canal Vingt</li>
    <li>Le Quotidien</li>
    <li><span class="sq"></span>Radio Ondes</li>
    <li><span class="sq green"></span></li>
  </ul>
</section>

<footer class="site-footer">
  <div class="wrap fcols">
    <div class="fcol"><h5>MENU</h5><ul><li>Nunc tempus felis</li><li>Vitae urna</li><li>Vivamus porttitor</li><li>Neque et volutpat</li><li>Rutrum lacus</li><li>Pro pharetra</li><li>Libero a tempus</li><li>Mattis lectus</li><li>Feugiat felis</li><li>Morbi diam</li><li>Lacus viverra</li></ul></div>
    <div class="fcol"><h5>TOPICS</h5><ul><li>Nunc tempus felis</li><li>Vitae urna</li><li>Vivamus porttitor</li><li>Neque et volutpat</li></ul><h5>INFO</h5><ul><li>Vitae urna</li><li>Vivamus porttitor</li><li>Neque et volutpat</li></ul></div>
    <div class="fcol"><h5>LINKS</h5><ul><li>Nunc tempus felis</li><li>Vitae urna</li><li>Vivamus porttitor</li><li>Neque et volutpat</li></ul><h5>RESOURCES</h5><ul><li>Nunc tempus felis</li><li>Vivamus porttitor</li><li>Neque et volutpat</li></ul></div>
    <div class="fcol"><h5>CATEGORY</h5><ul><li>Nunc tempus felis</li><li>Vitae urna</li><li>Vivamus porttitor</li><li>Neque et volutpat</li><li>Rutrum lacus</li><li>Pro pharetra</li><li>Libero a tempus</li><li>Mattis lectus</li><li>Feugiat felis</li><li>Morbi diam</li><li>Lacus viverra</li></ul></div>
    <div class="fcol"><h5>DOWNLOAD</h5><div class="store"></div><div class="store"></div></div>
  </div>
  <div class="copy">© 2018 Kora Télé. All rights reserved.</div>
</footer>
</body>
</html>
```